Letterhead, stationery and email signature for construction business

I need the letterhead, stationery and email signature designs for a construction business. I want them to have a corporate feel to them.

I've attached the logo for reference.

```html
<!DOCTYPE html>
<html lang="en">
<head>
<meta charset="utf-8">
<title>Halden Build – Stationery Set</title>
<link href="https://fonts.googleapis.com/css2?family=Lato:wght@400;700;900&display=swap" rel="stylesheet">
<style>
  :root {
    --backdrop: #c6c6c6;
    --paper: #ffffff;
    --brand-blue: #2b55a3;
    --brand-slate: #4a4a55;
    --ink: #222222;
    --ink-soft: #555555;
    --ghost: #f5f6f8;
    --ghost-grey: #d7d7d7;
    --shadow: 0 3px 8px rgba(0,0,0,0.22);
  }
  * { margin: 0; padding: 0; box-sizing: border-box; }
  html, body { width: 1199px; height: 1200px; overflow: hidden; }
  body {
    background: var(--backdrop);
    font-family: "Lato", Arial, sans-serif;
    color: var(--ink);
    position: relative;
  }
  .sheet { position: absolute; background: var(--paper); box-shadow: var(--shadow); overflow: hidden; }

  /* Wordmark */
  .wordmark { display: flex; align-items: center; gap: 7px; white-space: nowrap; }
  .wordmark__square { background: var(--brand-slate); flex: none; }
  .wordmark__name { font-weight: 900; color: var(--brand-blue); letter-spacing: 0.5px; line-height: 1; }

  /* Letterhead */
  .letterhead { left: 102px; top: 84px; width: 623px; height: 878px; }
  .letterhead__ghost { position: absolute; left: 155px; top: 108px; width: 420px; height: 610px; background: var(--ghost); }
  .letterhead .wordmark { position: absolute; top: 38px; left: 50%; transform: translateX(-50%); }
  .letterhead .wordmark__square { width: 26px; height: 26px; }
  .letterhead .wordmark__name { font-size: 26px; }
  .letterhead__footer { position: absolute; left: 0; right: 0; top: 817px; text-align: center; font-size: 13.5px; line-height: 19px; color: var(--ink); }
  .letterhead__footer strong { font-weight: 700; }
  .letterhead__bar { position: absolute; top: 828px; width: 142px; height: 14px; }
  .letterhead__bar--slate { left: 0; background: var(--brand-slate); }
  .letterhead__bar--blue { right: 0; background: var(--brand-blue); }

  /* Business card front */
  .card-front { left: 682px; top: 206px; width: 417px; height: 242px; }
  .card-front__art { position: absolute; inset: 0; }
  .card-front .wordmark { position: absolute; left: 47px; top: 44px; }
  .card-front .wordmark__square { width: 22px; height: 22px; }
  .card-front .wordmark__name { font-size: 22px; }
  .card-front__name { position: absolute; left: 47px; top: 110px; font-size: 18px; font-weight: 700; color: var(--ink); }
  .card-front__role { position: absolute; left: 47px; top: 133px; font-size: 10.5px; color: var(--ink-soft); }
  .contact-list { position: absolute; list-style: none; font-size: 11px; color: var(--ink-soft); }
  .contact-list li { display: flex; align-items: center; gap: 12px; height: 17px; }
  .contact-list svg { width: 8px; height: 9px; fill: var(--ink); flex: none; }
  .card-front .contact-list--main { left: 47px; top: 164px; }
  .card-front .contact-list--address { left: 243px; top: 182px; }
  .contact-list--address li { align-items: flex-start; height: auto; line-height: 17px; }
  .contact-list--address svg { margin-top: 4px; }

  /* Business card back */
  .card-back { left: 682px; top: 487px; width: 417px; height: 243px; }
  .card-back__ghost { position: absolute; left: 22px; top: -30px; width: 160px; height: 140px; background: var(--ghost-grey); transform: rotate(-18deg); }
  .card-back .wordmark { position: absolute; right: 44px; top: 172px; }
  .card-back .wordmark__square { width: 22px; height: 22px; }
  .card-back .wordmark__name { font-size: 22px; }

  /* Email signature */
  .signature { left: 411px; top: 984px; width: 627px; height: 147px; }
  .signature__art { position: absolute; inset: 0; }
  .signature .wordmark { position: absolute; left: 45px; top: 58px; }
  .signature .wordmark__square { width: 28px; height: 28px; }
  .signature .wordmark__name { font-size: 28px; }
  .signature__name { position: absolute; left: 362px; top: 30px; font-size: 16px; font-weight: 700; color: #fff; }
  .signature__role { position: absolute; left: 362px; top: 51px; font-size: 10px; color: #e6ebf5; }
  .signature__contact { position: absolute; left: 362px; top: 89px; font-size: 11px; line-height: 14.5px; color: #fff; }
</style>
</head>
<body>

  <section class="sheet letterhead" aria-label="Letterhead">
    <div class="letterhead__ghost"></div>
    <div class="wordmark">
      <span class="wordmark__square"></span>
      <span class="wordmark__name">HALDEN BUILD</span>
    </div>
    <div class="letterhead__bar letterhead__bar--slate"></div>
    <div class="letterhead__bar letterhead__bar--blue"></div>
    <div class="letterhead__footer">
      555-214-0000 | rc@haldenbuild.net | <strong>haldenbuild.net</strong><br>
      2200 Millbrook Ave. Fairview, RJ 00000
    </div>
  </section>

  <section class="sheet card-front" aria-label="Business card front">
    <svg class="card-front__art" viewBox="0 0 417 242" aria-hidden="true">
      <circle cx="480" cy="150" r="175" fill="var(--brand-blue)"/>
      <circle cx="300" cy="105" r="140" fill="var(--paper)"/>
      <ellipse cx="300" cy="0" rx="110" ry="38" fill="var(--brand-blue)"/>
    </svg>
    <div class="wordmark">
      <span class="wordmark__square"></span>
      <span class="wordmark__name">HALDEN BUILD</span>
    </div>
    <div class="card-front__name">Renata Coyle</div>
    <div class="card-front__role">Hair Stylist / Owner</div>
    <ul class="contact-list contact-list--main">
      <li><svg viewBox="0 0 8 9"><rect x="1.5" y="0" width="5" height="9" rx="1"/></svg>555-214-0000</li>
      <li><svg viewBox="0 0 8 9"><rect x="0" y="2" width="8" height="5"/></svg>rc@haldenbuild.net</li>
      <li><svg viewBox="0 0 8 9"><circle cx="4" cy="4.5" r="3.5"/></svg>haldenbuild.net</li>
    </ul>
    <ul class="contact-list contact-list--address">
      <li><svg viewBox="0 0 8 9"><path d="M4 0a3 3 0 0 1 3 3c0 2-3 6-3 6S1 5 1 3a3 3 0 0 1 3-3z"/></svg><span>2200 Millbrook Ave.<br>Fairview, RJ 00000</span></li>
    </ul>
  </section>

  <section class="sheet card-back" aria-label="Business card back">
    <div class="card-back__ghost"></div>
    <div class="wordmark">
      <span class="wordmark__square"></span>
      <span class="wordmark__name">HALDEN BUILD</span>
    </div>
  </section>

  <section class="sheet signature" aria-label="Email signature">
    <svg class="signature__art" viewBox="0 0 627 147" aria-hidden="true">
      <polygon points="265,0 551,0 507,66 310,66" fill="var(--brand-blue)"/>
      <polygon points="557,0 589,0 541,66 511,66" fill="var(--brand-slate)"/>
      <polygon points="293,81 311,81 270,147 249,147" fill="var(--brand-blue)"/>
      <polygon points="322,81 586,81 627,130 627,147 290,147" fill="var(--brand-slate)"/>
    </svg>
    <div class="wordmark">
      <span class="wordmark__square"></span>
      <span class="wordmark__name">HALDEN BUILD</span>
    </div>
    <div class="signature__name">Renata Coyle</div>
    <div class="signature__role">Hair Stylist / Owner</div>
    <div class="signature__contact">
      555-214-0000<br>
      rc@haldenbuild.net | haldenbuild.net<br>
      2200 Millbrook Ave. Fairview, RJ 00000
    </div>
  </section>

</body>
</html>
```